Retail Jewelry Business Card Design Project

We are in need of a new business card design for a retail jewelry store. This store is in the business of fine jewelry including but not specific to bridal jewelry, diamonds, designer jewelry and watches.

This store has been in business for 20 years but continues to strive for a modern professional appeal. The main colors use for this business are a royal blue, white and silver.

Target Market(s)

Target market is ages 18-50

Industry/Entity Type

Jewelry

Requirements
Must have
• Sales Person Name
Sales Person Email Address

Store Address
Store Phone
Website

Standard business card size. No odd shapes or sizes.
Nice to have
• Overall modern feel for card.

We have thought that a design with a nice feature of the logo on the back of the card would be nice but open to ideas.
Should not have
• No specific images of jewelry should be used.

```html
<!DOCTYPE html>
<html lang="en">
<head>
<meta charset="utf-8">
<title>Marlow Crane Fine Jewelry – Business Cards</title>
<link rel="stylesheet" href="https://fonts.googleapis.com/css2?family=Open+Sans:wght@400;700&display=swap">
<style>
  :root {
    --stage: #e6e6ea;
    --royal: #1c0f6b;
    --violet: #5a3fa8;
    --lavender: #d9cdee;
    --logo-ink: #3f3b8f;
    --ink: #0d0d12;
    --paper: #ffffff;
    --shadow: rgba(20, 20, 40, 0.35);
  }
  * { box-sizing: border-box; margin: 0; padding: 0; }
  html, body { width: 1200px; height: 838px; overflow: hidden; }
  body {
    background: var(--stage);
    font-family: "Open Sans", Arial, sans-serif;
    position: relative;
  }
  .card {
    position: absolute;
    top: 264px;
    width: 470px;
    height: 310px;
    border-radius: 22px;
    overflow: hidden;
    background: var(--paper);
    box-shadow: 0 10px 24px var(--shadow);
    border: 1.5px solid #111;
  }
  .card--front { left: 80px; }
  .card--back { left: 650px; }
  .card__art { position: absolute; inset: 0; width: 100%; height: 100%; }
  .card__url {
    position: absolute;
    right: 18px;
    bottom: 22px;
    font-size: 8px;
    color: var(--paper);
  }
  .brand {
    position: absolute;
    color: var(--logo-ink);
    font-weight: 700;
    text-align: center;
    line-height: 1.1;
  }
  .brand--large { left: 70px; right: 30px; top: 100px; }
  .brand--large .brand__name { font-size: 46px; letter-spacing: 0.5px; }
  .brand--large .brand__line { font-size: 20px; letter-spacing: 2px; margin-top: 6px; }
  .brand--small { right: 20px; top: 22px; }
  .brand--small .brand__name { font-size: 15px; }
  .brand--small .brand__line { font-size: 7px; letter-spacing: 1px; }
  .contact { position: absolute; left: 36px; top: 68px; color: var(--ink); }
  .contact__name { font-size: 21px; font-weight: 700; line-height: 1.2; margin-bottom: 6px; }
  .contact__line { font-size: 12.5px; line-height: 1.3; }
  .contact__person { font-weight: 700; }
  .contact__web { font-size: 13.5px; margin-top: 6px; }
</style>
</head>
<body>

<svg width="0" height="0" style="position:absolute" aria-hidden="true">
  <defs>
    <linearGradient id="paper-tint" x1="0" y1="0" x2="1" y2="1">
      <stop offset="0.45" stop-color="#ffffff"/>
      <stop offset="1" stop-color="#d8ceea"/>
    </linearGradient>
    <linearGradient id="swoosh-fill" x1="0" y1="0" x2="1" y2="0">
      <stop offset="0" stop-color="#c9b9e6"/>
      <stop offset="0.6" stop-color="#6a4cb3"/>
      <stop offset="1" stop-color="#1c0f6b"/>
    </linearGradient>
    <linearGradient id="band-fill" x1="0" y1="0" x2="1" y2="0.3">
      <stop offset="0" stop-color="#efe9f8"/>
      <stop offset="0.45" stop-color="#9c83d0"/>
      <stop offset="0.62" stop-color="#1c0f6b"/>
      <stop offset="1" stop-color="#1c0f6b"/>
    </linearGradient>
    <clipPath id="front-corner">
      <path d="M0 0 L260 0 Q60 8 0 150 Z"/>
    </clipPath>
    <clipPath id="back-corner">
      <path d="M0 0 L380 0 Q90 4 0 84 Z"/>
    </clipPath>
  </defs>
</svg>

<div class="card card--front">
  <svg class="card__art" viewBox="0 0 470 310" preserveAspectRatio="none" aria-hidden="true">
    <rect width="470" height="310" fill="url(#paper-tint)"/>
    <g class="card__stripes" stroke="#5a3fa8" stroke-width="3" clip-path="url(#front-corner)">
      <line x1="0" y1="12" x2="80" y2="12"/>
      <line x1="0" y1="22" x2="80" y2="22"/>
      <line x1="0" y1="32" x2="80" y2="32"/>
      <line x1="0" y1="42" x2="80" y2="42"/>
      <line x1="0" y1="52" x2="80" y2="52"/>
      <line x1="0" y1="62" x2="80" y2="62"/>
      <line x1="0" y1="72" x2="80" y2="72"/>
      <line x1="0" y1="82" x2="80" y2="82"/>
      <line x1="0" y1="92" x2="80" y2="92"/>
      <line x1="0" y1="102" x2="80" y2="102"/>
      <line x1="0" y1="112" x2="80" y2="112"/>
    </g>
    <path d="M60 0 L260 0 Q60 8 0 150 L0 118 Q14 30 60 0 Z" fill="url(#swoosh-fill)"/>
    <path d="M260 1 Q60 10 0 156" fill="none" stroke="#1c0f6b" stroke-width="2.5"/>
    <rect x="0" y="253" width="470" height="4" fill="#1c0f6b"/>
    <rect x="0" y="257" width="470" height="3" fill="#ffffff"/>
    <rect x="0" y="260" width="470" height="50" fill="url(#band-fill)"/>
  </svg>
  <div class="brand brand--large">
    <div class="brand__name">Marlow Crane</div>
    <div class="brand__line">FINE JEWELRY</div>
  </div>
  <p class="card__url">www.marlowcranejewelry.com</p>
</div>

<div class="card card--back">
  <svg class="card__art" viewBox="0 0 470 310" preserveAspectRatio="none" aria-hidden="true">
    <rect width="470" height="310" fill="url(#paper-tint)"/>
    <g class="card__stripes" stroke="#5a3fa8" stroke-width="3" clip-path="url(#back-corner)">
      <line x1="0" y1="12" x2="70" y2="12"/>
      <line x1="0" y1="22" x2="70" y2="22"/>
      <line x1="0" y1="32" x2="70" y2="32"/>
      <line x1="0" y1="42" x2="70" y2="42"/>
      <line x1="0" y1="52" x2="70" y2="52"/>
    </g>
    <path d="M50 0 L380 0 Q90 4 0 84 L0 62 Q16 14 50 0 Z" fill="url(#swoosh-fill)"/>
    <path d="M380 1 Q90 6 0 90" fill="none" stroke="#1c0f6b" stroke-width="2.5"/>
    <rect x="0" y="220" width="470" height="4" fill="#1c0f6b"/>
    <rect x="0" y="224" width="470" height="3" fill="#ffffff"/>
    <rect x="0" y="227" width="470" height="83" fill="url(#band-fill)"/>
  </svg>
  <div class="brand brand--small">
    <div class="brand__name">Marlow Crane</div>
    <div class="brand__line">FINE JEWELRY</div>
  </div>
  <div class="contact">
    <h1 class="contact__name">Marlow Crane Fine</h1>
    <p class="contact__line contact__person">Elena Marsh, Sales Associate</p>
    <p class="contact__line">2280 Linden Avenue</p>
    <p class="contact__line">Harbor Falls, FL 32590</p>
    <p class="contact__line">Phone: (850) 555-0147</p>
    <p class="contact__line">Email: info@marlowcranejewelry.com</p>
    <p class="contact__web">www.marlowcranejewelry.com</p>
  </div>
  <p class="card__url">www.marlowcranejewelry.com</p>
</div>

</body>
</html>
```